Prosthetic Brochure

Looking for a trifold brochure that highlights our Prosthetic department. Has to have good stock pictures of prosthetic care. Should have Prosthetic Services from our website www.brindlemoorclinic.com I would like it in the same colors of our website.

Target Market(s)

Patients and physicians

Industry/Entity Type

Medical

Requirements
Must have
• Pictures of people helping prosthetic patients and information from the flyer I uploaded and our website under Prosthetic services.
Nice to have
• Same color scheme as our website. Blue with orange highlights
Should not have
• Just prosthetics no pictures of braces ( orthotics)

```html
<!DOCTYPE html>
<html lang="en">
<head>
<meta charset="utf-8">
<title>Brindlemoor Limb Clinic – Prosthetic Team Brochure</title>
<link href="https://fonts.googleapis.com/css2?family=Montserrat:wght@600;800&family=Oswald:wght@500;600&family=Open+Sans:ital,wght@0,400;0,600;0,700;1,400&display=swap" rel="stylesheet">
<style>
:root{
  --blue:#1d3fb8;
  --blue-deep:#18329a;
  --orange:#ee4313;
  --ink:#333a44;
  --grey:#5c6470;
  --paper:#ffffff;
  --stage:#eceef1;
}
*{box-sizing:border-box;margin:0;padding:0}
html,body{width:1200px;height:2399px;overflow:hidden;background:var(--stage);font-family:"Open Sans",Arial,sans-serif;color:var(--ink)}
.spread{position:absolute;left:50px;width:1100px;height:850px;background:var(--paper);box-shadow:0 14px 40px rgba(0,0,0,.16);display:flex}
.spread--outside{top:233px}
.spread--inside{top:1233px}
.panel{position:relative;width:366.67px;height:850px;overflow:hidden}
.panel+.panel{border-left:1px solid #e3e5e9}

/* shared */
.band{position:absolute;left:0;right:0;bottom:0;height:58px;background:var(--orange);border-top:6px solid var(--blue);display:flex;align-items:center;justify-content:center}
.url{font-family:"Montserrat",sans-serif;font-weight:600;color:#fff;font-size:17px;letter-spacing:.5px}
.brand{font-family:"Montserrat",sans-serif;font-weight:800;color:var(--blue);display:flex;align-items:center;gap:10px;justify-content:center}
.brand__dot{width:16px;height:16px;border-radius:50%;background:var(--blue);flex:none}
.photo{background:linear-gradient(135deg,#8a6a5a,#4e6f9a 55%,#c9b7a0)}

/* back panel */
.back__top{position:absolute;left:0;top:0;width:100%;height:740px;background:var(--blue);border-top:28px solid var(--orange)}
.back__badge{position:absolute;left:123px;top:56px;width:120px;height:120px;border-radius:50%;background:#fff;border:8px solid #dfe5f7}
.back__text{position:absolute;left:32px;right:32px;top:196px;color:#fff;font-size:12.5px;line-height:1.55;font-style:italic;text-align:center}
.callbar{display:inline-flex;align-items:center;gap:8px;background:var(--orange);color:#fff;font-family:"Oswald",sans-serif;font-weight:600;font-size:20px;padding:4px 14px;font-style:italic}
.callbar svg{width:18px;height:18px;fill:#fff}
.back__call{position:absolute;left:50%;transform:translateX(-50%);top:448px;white-space:nowrap}
.back__photo{position:absolute;left:34px;right:34px;top:510px;height:200px;border:6px solid #fff;box-shadow:0 4px 10px rgba(0,0,0,.25);background:linear-gradient(135deg,#dfe8d2,#9fbf86 50%,#e8ede4)}

/* locations panel */
.locations{position:absolute;left:40px;right:40px;top:70px;text-align:center}
.locations__title{font-family:"Oswald",sans-serif;font-style:italic;font-weight:600;color:var(--orange);font-size:20px;letter-spacing:1px;margin-bottom:14px}
.locations__item{font-size:13.5px;line-height:1.45;color:var(--ink);font-style:italic;margin-bottom:14px}
.mid__brand{position:absolute;left:0;right:0;top:600px;font-size:19px}
.mid__call{position:absolute;left:0;right:0;bottom:58px;height:54px;background:var(--blue);display:flex;align-items:center;justify-content:center;gap:10px;color:#fff;font-family:"Oswald",sans-serif;font-weight:600;font-style:italic;font-size:26px}
.mid__call svg{width:22px;height:22px;fill:#fff}

/* cover */
.cover__shapes{position:absolute;inset:0;width:366.67px;height:850px}
.cover__brand{position:absolute;left:0;right:0;top:95px;font-size:21px}
.cover__photo{position:absolute;inset:0;clip-path:path("M0,282 Q190,268 367,178 L367,560 Q200,606 0,592 Z")}
.cover__title{position:absolute;left:0;right:0;top:630px;text-align:center;font-family:"Montserrat",sans-serif;font-weight:800;color:var(--blue);font-size:27px;line-height:1.15;letter-spacing:1px}
.cover__tagline{position:absolute;left:0;right:0;top:710px;text-align:center;font-family:"Oswald",sans-serif;font-style:italic;font-weight:500;color:var(--orange);font-size:17px}

/* inside */
.inside__band{position:absolute;left:0;right:0;bottom:0;height:58px;background:var(--orange);border-top:6px solid var(--blue);display:flex;align-items:center;justify-content:flex-end;padding-right:40px;z-index:2}
.why{padding:46px 34px 0}
.why__title{display:inline-block;background:var(--blue);color:#fff;font-family:"Oswald",sans-serif;font-weight:600;font-size:17px;padding:5px 16px;border-radius:16px 0 16px 0;margin-bottom:20px}
.why__item{margin-bottom:15px}
.why__head{font-family:"Montserrat",sans-serif;font-weight:800;color:var(--orange);font-size:14.5px}
.why__body{font-size:12px;line-height:1.45;color:var(--grey)}
.why__note{font-size:11.5px;font-weight:700;font-style:italic;color:var(--blue);text-align:center;margin:4px 0 16px}
.why__cta{font-family:"Oswald",sans-serif;font-weight:600;color:var(--blue);font-size:22px;line-height:1.15;text-align:center}

.team{padding:40px 28px 0;display:flex;flex-direction:column;gap:26px}
.member{display:grid;grid-template-columns:88px 1fr;column-gap:14px;row-gap:8px;align-items:center}
.member__photo{width:88px;height:88px;border-radius:50%;border:4px solid #fff;box-shadow:0 2px 8px rgba(0,0,0,.2);background:radial-gradient(circle at 50% 40%,#d9b9a2,#7a5f50 70%)}
.member__name{font-family:"Montserrat",sans-serif;font-weight:800;color:var(--blue);font-size:13px;line-height:1.25}
.member__cred{display:block;font-weight:600;font-size:11.5px;font-style:italic}
.member__bio{grid-column:1/3;font-size:11.5px;line-height:1.5;color:var(--grey)}
</style>
</head>
<body>

<!-- OUTSIDE SPREAD -->
<section class="spread spread--outside">
  <article class="panel panel--back">
    <div class="back__top"></div>
    <div class="back__badge" role="img" aria-label="Certification badge"></div>
    <p class="back__text">Brindlemoor Limb Clinic has been providing quality, compassionate care to residents of the region since 1983. A recognized leader in the field, our experts work as a team to create the most functional solution to your prosthetic needs using the latest technology available. Our patient-centered team approach means we work closely with your doctor, nurse, therapist and family to deliver a great fitting prosthetic device that works for you.</p>
    <span class="callbar back__call"><svg viewBox="0 0 24 24"><path d="M6.6 10.8a15 15 0 0 0 6.6 6.6l2.2-2.2c.3-.3.7-.4 1-.2 1.1.4 2.3.6 3.6.6.6 0 1 .4 1 1V20c0 .6-.4 1-1 1A17 17 0 0 1 3 4c0-.6.4-1 1-1h3.5c.6 0 1 .4 1 1 0 1.3.2 2.5.6 3.6.1.3 0 .7-.2 1z"/></svg>Call Us - 555-014-2200</span>
    <div class="back__photo" role="img" aria-label="Photo of a person holding hands with someone wearing a prosthetic arm outdoors"></div>
    <div class="band"><span class="url">www.brindlemoorclinic.com</span></div>
  </article>

  <article class="panel panel--locations">
    <div class="locations">
      <h3 class="locations__title">LOCATIONS</h3>
      <p class="locations__item">210 Alder Lane<br>Fenwick Grove 40112<br>PH. (555) 014-2200</p>
      <p class="locations__item">Riverside Care Pavilion<br>88 Quay Street, Suite 4B<br>Hollin 40118<br>PH. (555) 014-2311</p>
      <p class="locations__item">415 Crestmoor Road, Suite 12<br>Ashby 40121<br>PH. (555) 014-2422</p>
      <p class="locations__item">1930 Linden Court, Ste 7<br>Marlow Bay 40130<br>PH. (555) 014-2533</p>
      <p class="locations__item">6 Heron Terrace, Ste 2<br>Dunmore 40135<br>PH. (555) 014-2644</p>
    </div>
    <div class="brand mid__brand"><span class="brand__dot"></span>Brindlemoor Limb Clinic</div>
    <div class="mid__call"><svg viewBox="0 0 24 24"><path d="M6.6 10.8a15 15 0 0 0 6.6 6.6l2.2-2.2c.3-.3.7-.4 1-.2 1.1.4 2.3.6 3.6.6.6 0 1 .4 1 1V20c0 .6-.4 1-1 1A17 17 0 0 1 3 4c0-.6.4-1 1-1h3.5c.6 0 1 .4 1 1 0 1.3.2 2.5.6 3.6.1.3 0 .7-.2 1z"/></svg>Call Us - 555-014-2200</div>
    <div class="band"><span class="url">www.brindlemoorclinic.com</span></div>
  </article>

  <article class="panel panel--cover">
    <svg class="cover__shapes" viewBox="0 0 366.67 850" aria-hidden="true">
      <path d="M0,252 Q190,240 367,146 L367,178 Q190,268 0,282 Z" fill="#ee4313"/>
      <path d="M0,592 Q200,606 367,560 L367,574 Q200,622 0,606 Z" fill="#1d3fb8"/>
    </svg>
    <div class="brand cover__brand"><span class="brand__dot"></span>Brindlemoor Limb Clinic</div>
    <div class="cover__photo photo" role="img" aria-label="Group photo of the prosthetic team standing in front of a brick building"></div>
    <h1 class="cover__title">MEET OUR<br>PROSTHETIC TEAM</h1>
    <p class="cover__tagline">We're Making A Difference in People's Lives...</p>
    <div class="band"><span class="url">www.brindlemoorclinic.com</span></div>
  </article>
</section>

<!-- INSIDE SPREAD -->
<section class="spread spread--inside">
  <article class="panel why">
    <h2 class="why__title">Why use Brindlemoor Limb Clinic?</h2>
    <div class="why__item"><h3 class="why__head">First-class patient care -</h3><p class="why__body">Our facility is accredited by a national board for prosthetic care. We meet strict standards that put patient needs and safety first.</p></div>
    <div class="why__item"><h3 class="why__head">High-end technology -</h3><p class="why__body">We are always current on the latest socket and component technology.</p></div>
    <div class="why__item"><h3 class="why__head">Local Fabrication Facility -</h3><p class="why__body">Our fabrication and assembly happens right here in our own lab.</p></div>
    <div class="why__item"><h3 class="why__head">Experience -</h3><p class="why__body">78 years of combined technical &amp; practitioner experience.</p></div>
    <div class="why__item"><h3 class="why__head">Fast turnaround -</h3><p class="why__body">Same week check sockets, complete definitive prosthesis in 30 days (pending insurance authorizations).</p></div>
    <div class="why__item"><h3 class="why__head">A firm belief in teamwork -</h3><p class="why__body">We love to work with the patient, rehabilitative staff and physicians to achieve the patient's goals.</p></div>
    <p class="why__note">All of these combined allow us to provide the best possible patient outcome.</p>
    <p class="why__cta">Call us today for a free consult<br>and prosthetic check-up<br>Call (555) 014-2200</p>
  </article>

  <article class="panel team">
    <div class="member">
      <div class="member__photo" role="img" aria-label="Portrait of Owen Marsh"></div>
      <h3 class="member__name">OWEN MARSH, CPO<span class="member__cred">Board Certified<br>Prosthetist &amp; Orthotist</span></h3>
      <p class="member__bio">Owen holds dual Master's Degrees in Prosthetics and Orthotics and in Business Administration. His undergrad was in athletic training. Owen keeps up to date on the latest cutting edge prosthetic technology and loves the progress being made in prosthetics.</p>
    </div>
    <div class="member">
      <div class="member__photo" role="img" aria-label="Portrait of Lena Forde"></div>
      <h3 class="member__name">LENA FORDE, CPO<span class="member__cred">Board Certified<br>Prosthetist &amp; Orthotist</span></h3>
      <p class="member__bio">Lena graduated from Hollin State University with her Master of Science in Prosthetics and Orthotics. She has been practicing since 2018. Lena is a people person and loves working with patients.</p>
    </div>
    <div class="member">
      <div class="member__photo" role="img" aria-label="Portrait of Nico Barlow"></div>
      <h3 class="member__name">NICO BARLOW, CPO<span class="member__cred">Board Certified<br>Prosthetist &amp; Orthotist</span></h3>
      <p class="member__bio">Nico grew up locally and graduated in biomedical engineering. He earned a Master's Degree in Prosthetics and Orthotics. His hobbies include playing soccer and he is passionate about helping others.</p>
    </div>
  </article>

  <article class="panel team">
    <div class="member">
      <div class="member__photo" role="img" aria-label="Portrait of Walter Hensley"></div>
      <h3 class="member__name">WALTER HENSLEY, CPO<span class="member__cred">Board Certified<br>Prosthetist &amp; Orthotist</span></h3>
      <p class="member__bio">With over 46 years of prosthetic experience, Walter has been a leader and past president of our national organization and is highly respected for his experience and knowledge.</p>
    </div>
    <div class="member">
      <div class="member__photo" role="img" aria-label="Portrait of Ruth Calder"></div>
      <h3 class="member__name">RUTH CALDER, CPO<span class="member__cred">Board Certified<br>Prosthetist &amp; Orthotist</span></h3>
      <p class="member__bio">Ruth graduated with her Master's Degree in Prosthetics and Orthotics. She did her undergrad in biomedical engineering. Ruth is a local native and loves this city.</p>
    </div>
    <div class="member">
      <div class="member__photo" role="img" aria-label="Portrait of Evan Pryce"></div>
      <h3 class="member__name">EVAN PRYCE, CPO<span class="member__cred">Board Certified<br>Orthotist &amp; Prosthetist</span></h3>
      <p class="member__bio">Evan graduated with a Master Degree in Prosthetics and Orthotics. His undergrad is in exercise physiology. Evan is a huge outdoor enthusiast and loves helping people regain their independence.</p>
    </div>
  </article>

  <div class="inside__band"><span class="url">www.brindlemoorclinic.com</span></div>
</section>

</body>
</html>
```